to-go container produts catalogue

we sell different kinds of to-go containers and need to make a catalogue for our cosumers.
Most of them are restraunts owner and some of them are distrunutors.
Our company named "Bright Meadow Packaging"
Our website is www.brightmeadowpackaging.com
our produts are quite like we showed on web.
We also have other produtcs need to be showed in the catalogue
We have different product lines and each type have different size.
We hope the catalogue is simple and clear. maybe a little industrial style

```html
<!DOCTYPE html>
<html lang="en">
<head>
<meta charset="utf-8">
<title>Bright Meadow Packaging – Catalogue</title>
<link href="https://fonts.googleapis.com/css2?family=Baloo+2:wght@600;700&family=Nunito:wght@400;600&display=swap" rel="stylesheet">
<style>
:root{
  --backdrop:#d0d0d0;
  --paper:#ffffff;
  --mint:#a8dfc0;
  --mint-soft:#d6f0e2;
  --mint-pale:#e9f7ef;
  --green:#5fb58a;
  --green-deep:#3f8f68;
  --border:#7fbf9c;
  --ink:#2b2b2b;
  --ink-soft:#555;
  --brand-blue:#1f6fa8;
  --photo-a:#7fd0aa;
  --photo-b:#c9ead8;
}
*{box-sizing:border-box;margin:0;padding:0}
html,body{width:803px;height:1200px;overflow:hidden;background:var(--backdrop)}
body{position:relative;font-family:"Nunito",sans-serif;color:var(--ink)}
.spread{position:absolute;left:48px;width:715px;height:359px;display:flex;gap:2px}
.page{position:relative;width:356.5px;height:359px;background:var(--paper);overflow:hidden}
.spread--cover{top:40px}.spread--products{top:414px}.spread--extras{top:796px}

.photo{position:absolute;background:linear-gradient(135deg,var(--photo-a),var(--photo-b) 55%,var(--photo-a))}
.photo--frame{left:12px;top:12px;width:333px;height:333px}
.photo--cover{left:12px;top:12px;width:333px;height:333px}
.intro{position:absolute;left:92px;top:92px;width:173px;height:168px;background:var(--paper);border-radius:10px;text-align:center;font-size:5.6px;line-height:7.8px;padding:9px 6px 0}
.intro p{margin-bottom:7px}
.intro .contact{margin-top:4px}
.intro svg{display:block;margin:0 auto 2px;width:7px;height:7px;fill:var(--ink)}
.intro .contact div{margin-bottom:9px}
.brand-box{position:absolute;left:108px;top:262px;width:150px;height:90px;background:var(--paper);display:flex;align-items:center;justify-content:center;gap:6px}
.brand-box .mark{width:12px;height:12px;background:var(--brand-blue)}
.brand-name{font-family:"Baloo 2",sans-serif;font-weight:700;font-size:15px;line-height:15px;color:var(--brand-blue);width:110px}

.band{position:absolute;top:10px;height:24px;background:linear-gradient(90deg,var(--green),var(--mint) 60%,var(--mint-soft));font-family:"Baloo 2",sans-serif;font-weight:700;color:#fff;font-size:11px;line-height:26px}
.band--left{left:12px;width:336px;clip-path:polygon(0 0,100% 0,94% 100%,0 100%);padding-left:37px}
.band--right{left:9px;width:336px;clip-path:polygon(6% 0,100% 0,100% 100%,0 100%);background:linear-gradient(270deg,var(--green),var(--mint) 60%,var(--mint-soft));text-align:right;padding-right:50px}

.card{position:absolute;width:162px;height:141px;border:1.2px solid var(--border);border-radius:6px;overflow:hidden;background:#fff}
.card__title{height:24px;background:var(--mint);font-size:7.3px;line-height:7.6px;text-align:center;display:flex;align-items:center;justify-content:center;padding:0 3px}
.card__photo{height:61px;display:flex;align-items:center;justify-content:center}
.card__photo div{width:92px;height:46px;border-radius:8px}
.shot-black{background:linear-gradient(160deg,#6b6b6b,#1e1e1e)}
.shot-white{background:linear-gradient(160deg,#ffffff,#e3e3e3);border:1px solid #ddd}
.card__specs{height:56px;background:var(--mint-soft);display:flex;padding:4px 5px 0 5px}
.specs{flex:1;font-size:5.1px;line-height:6px;color:var(--ink)}
.badges{width:62px;display:grid;grid-template-columns:1fr 1fr;row-gap:2px;text-align:center;font-size:3.8px;font-weight:600;line-height:4px}
.badges svg{display:block;margin:0 auto 1px;width:12px;height:12px;stroke:var(--ink);fill:none;stroke-width:1.2}

.pitch{position:absolute;left:12px;top:47px;width:300px;font-size:8.6px;line-height:10px;color:var(--ink)}
.pitch .kicker{display:inline-block;background:var(--mint);color:var(--ink-soft);padding:0 4px;margin-bottom:10px}
.pitch p{margin-bottom:10px;padding-left:4px}
.pitch strong{color:var(--green-deep);font-weight:700;display:block}
.pitch .narrow{width:140px}
.collage{position:absolute;left:0;top:0;width:356.5px;height:359px}

.news-col{position:absolute;top:42px;width:160px;height:303px;border:.6px solid #bbb;padding:3px 4px;font-size:6px;line-height:6.6px;text-align:justify;color:var(--ink-soft)}
.news-col h3{background:var(--mint);font-family:"Nunito",sans-serif;font-weight:600;color:#fff;font-size:7.8px;line-height:9px;padding-left:3px;margin-bottom:2px}
.news-col p{margin-bottom:0}
.news-col .wrap{height:158px}
.news-photo{position:absolute;left:91px;top:105px;width:169px;height:156px;background:linear-gradient(150deg,#f4f4f4,#cfcfcf 45%,#2a2a2a 70%,#e06a3c)}
</style>
</head>
<body>
<svg width="0" height="0" style="position:absolute">
  <symbol id="i-leak" viewBox="0 0 12 12"><circle cx="6" cy="6" r="5"/><path d="M2.5 9.5 9.5 2.5M6 3.5c-1.5 2-2 3-2 4a2 2 0 0 0 4 0c0-1-.5-2-2-4z"/></symbol>
  <symbol id="i-recycle" viewBox="0 0 12 12"><path d="M6 1.5 10.5 9.5H1.5z"/><path d="M4.5 4.5 6 2M7.5 7.5h3M3 9.5 1.5 7"/></symbol>
  <symbol id="i-bpa" viewBox="0 0 12 12"><circle cx="6" cy="6" r="5"/><circle cx="6" cy="6" r="3.2"/></symbol>
  <symbol id="i-micro" viewBox="0 0 12 12"><rect x="1.5" y="3" width="9" height="6.5" rx="1"/><rect x="2.8" y="4.3" width="5" height="4"/></symbol>
</svg>

<!-- Cover spread -->
<section class="spread spread--cover">
  <div class="page">
    <div class="photo photo--frame" role="img" aria-label="Mosaic of disposable cutlery, cups, kraft boxes and salad bowls on mint background"></div>
    <div class="intro">
      <p>We at Bright Meadow Packaging are committed to providing high quality disposable goods to our customers. We are a small business based in Los Angeles, California. We specialize in customization of cutlery, napkins, and other disposables.</p>
      <p>Contact us 24/7 our team of sales is ready to serve.</p>
      <div class="contact">
        <div><svg viewBox="0 0 10 10"><path d="M5 0a3.5 3.5 0 0 0-3.5 3.5C1.5 6 5 10 5 10s3.5-4 3.5-6.5A3.5 3.5 0 0 0 5 0zm0 5a1.5 1.5 0 1 1 0-3 1.5 1.5 0 0 1 0 3z"/></svg>1875 Orchard Row<br>Fairdale, CA 90210</div>
        <div><svg viewBox="0 0 10 10"><path d="M2 0 4 2.5 3 4c.8 1.4 1.6 2.2 3 3l1.5-1L10 8 8.5 10C4 9.5.5 6 0 1.5z"/></svg>555-214-3080</div>
        <div><svg viewBox="0 0 10 10"><path d="M0 2h10v6H0z M0 2l5 3.5L10 2" stroke="#fff" stroke-width=".6"/></svg>cs@brightmeadowpackaging.com</div>
      </div>
    </div>
  </div>
  <div class="page">
    <div class="photo photo--cover" role="img" aria-label="Mosaic of mint takeout containers, cups, lids and kraft boxes"></div>
    <div class="brand-box"><span class="mark"></span><span class="brand-name">Bright Meadow Packaging</span></div>
  </div>
</section>

<!-- Products spread -->
<section class="spread spread--products">
  <div class="page">
    <div class="band band--left">Microwaveable Take-Out Containers</div>

    <article class="card" style="left:11px;top:47px">
      <h3 class="card__title" style="font-weight:400">58oz Microwaveable<br>Container with Lid, 150 sets</h3>
      <div class="card__photo"><div class="shot-black" role="img" aria-label="Black rectangular container with clear lid"></div></div>
      <div class="card__specs"><div class="specs">Color:Black/White Base,<br>Clear Lid<br>Capacity:58 oz<br>Material:PP<br>Product Weight:84g ± 1g<br>Case Pack:150<br>Case Weight:28.68 lb<br>Case Dimension:62.5*29*34.5 cm</div>
        <div class="badges"><div><svg><use href="#i-leak"/></svg>LEAK PROOF</div><div><svg><use href="#i-recycle"/></svg>RECYCLABLE</div><div><svg><use href="#i-bpa"/></svg>BPA FREE</div><div><svg><use href="#i-micro"/></svg>MICROWAVE SAFE</div></div></div>
    </article>

    <article class="card" style="left:184px;top:47px">
      <h3 class="card__title" style="font-weight:400">48oz Square Microwaveable<br>Container with Lid 3-compartment, 100 sets</h3>
      <div class="card__photo"><div class="shot-black" style="width:66px;height:54px" role="img" aria-label="Black square three-compartment container"></div></div>
      <div class="card__specs"><div class="specs">Color:Black/White Base,<br>Clear Lid<br>Capacity:48 oz<br>Material:PP<br>Product Weight:84g ± 1g<br>Case Pack:100<br>Case Weight:19.4 lb<br>Case Dimension:42.5*21.8*43.7 cm</div>
        <div class="badges"><div><svg><use href="#i-leak"/></svg>LEAK PROOF</div><div><svg><use href="#i-recycle"/></svg>RECYCLABLE</div><div><svg><use href="#i-bpa"/></svg>BPA FREE</div><div><svg><use href="#i-micro"/></svg>MICROWAVE SAFE</div></div></div>
    </article>

    <article class="card" style="left:11px;top:201px">
      <h3 class="card__title" style="font-weight:400">39oz Rectangular Microwaveable<br>Container with Lid 3-compartment, 150 sets</h3>
      <div class="card__photo"><div class="shot-black" role="img" aria-label="Black three-compartment rectangular container"></div></div>
      <div class="card__specs"><div class="specs">Color:Black/White Base,<br>Clear Lid<br>Capacity:39 oz<br>Material:PP<br>Product Weight:72g ± 1g<br>Case Pack:150<br>Case Weight:25.88 lb<br>Case Dimension:59*25.5*39 cm</div>
        <div class="badges"><div><svg><use href="#i-leak"/></svg>LEAK PROOF</div><div><svg><use href="#i-recycle"/></svg>RECYCLABLE</div><div><svg><use href="#i-bpa"/></svg>BPA FREE</div><div><svg><use href="#i-micro"/></svg>MICROWAVE SAFE</div></div></div>
    </article>

    <article class="card" style="left:184px;top:201px">
      <h3 class="card__title" style="font-weight:400">38oz Rectangular Microwaveable<br>Container with Lid, 150 sets</h3>
      <div class="card__photo"><div class="shot-black" role="img" aria-label="Black deep rectangular container with clear lid"></div></div>
      <div class="card__specs"><div class="specs">Color:Black/White Base,<br>Clear Lid<br>Capacity:38 oz<br>Material:PP<br>Product Weight:54g ± 1g<br>Case Pack:150<br>Case Weight:17.35 lb<br>Case Dimension:48*23.7*48 cm</div>
        <div class="badges"><div><svg><use href="#i-leak"/></svg>LEAK PROOF</div><div><svg><use href="#i-recycle"/></svg>RECYCLABLE</div><div><svg><use href="#i-bpa"/></svg>BPA FREE</div><div><svg><use href="#i-micro"/></svg>MICROWAVE SAFE</div></div></div>
    </article>
  </div>

  <div class="page">
    <div class="band band--right">Clamshell Contaier</div>

    <article class="card" style="left:9px;top:46px">
      <h3 class="card__title" style="font-weight:400">Clamshell Container 3-Compartment,<br>Center Slide, 9.5"x 9.25"</h3>
      <div class="card__photo"><div class="shot-white" style="width:58px;height:56px" role="img" aria-label="White three-compartment foam clamshell"></div></div>
      <div class="card__specs"><div class="specs"><br>Color: White<br>Capacity:36 oz<br>Material:MFPP<br>Case Pack:150 Sets<br>Case Weight:22.05 lb<br>Case Dimension:<br>20.08"x11.02"x10.04"</div>
        <div class="badges"><div><svg><use href="#i-leak"/></svg>LEAK PROOF</div><div><svg><use href="#i-recycle"/></svg>RECYCLABLE</div><div><svg><use href="#i-bpa"/></svg>BPA FREE</div><div><svg><use href="#i-micro"/></svg>MICROWAVE SAFE</div></div></div>
    </article>

    <article class="card" style="left:182px;top:46px">
      <h3 class="card__title" style="font-weight:400">Clamshell Container,<br>Center Slide, 9.5"x9.25"</h3>
      <div class="card__photo"><div class="shot-white" style="width:58px;height:56px" role="img" aria-label="White single-compartment clamshell"></div></div>
      <div class="card__specs"><div class="specs"><br>Color: White<br>Capacity:40 oz<br>Material:MFPP<br>Case Pack:150 Sets<br>Case Weight:22.05 lb<br>Case Dimension:<br>20.47x11.02"x10.04"</div>
        <div class="badges"><div><svg><use href="#i-leak"/></svg>LEAK PROOF</div><div><svg><use href="#i-recycle"/></svg>RECYCLABLE</div><div><svg><use href="#i-bpa"/></svg>BPA FREE</div><div><svg><use href="#i-micro"/></svg>MICROWAVE SAFE</div></div></div>
    </article>

    <article class="card" style="left:9px;top:200px">
      <h3 class="card__title" style="font-weight:400">Clamshell Container 3-Compartment,<br>Corner Lock, 9"x 9"</h3>
      <div class="card__photo"><div class="shot-white" style="width:66px;height:56px" role="img" aria-label="Open white clamshell with corner lock"></div></div>
      <div class="card__specs"><div class="specs"><br>Color: White<br>Capacity:25 oz<br>Material:MFPP<br>Case Pack:150 Sets<br>Case Weight:22 lb<br>Case Dimension:<br>17.72"x17.72"x9.45</div>
        <div class="badges"><div><svg><use href="#i-leak"/></svg>LEAK PROOF</div><div><svg><use href="#i-recycle"/></svg>RECYCLABLE</div><div><svg><use href="#i-bpa"/></svg>BPA FREE</div><div><svg><use href="#i-micro"/></svg>MICROWAVE SAFE</div></div></div>
    </article>

    <article class="card" style="left:182px;top:200px">
      <h3 class="card__title" style="font-weight:400">Clamshell Container, Center Slide,<br>8.8"x5.3"</h3>
      <div class="card__photo"><div class="shot-white" style="width:78px;height:50px" role="img" aria-label="White rectangular clamshell"></div></div>
      <div class="card__specs"><div class="specs"><br>Color: White<br>Capacity:24 oz<br>Material:MFPP<br>Case Pack:200 Sets<br>Case Weight:19.18 lb<br>Case Dimension:<br>15.75"x12.40"x9.45"</div>
        <div class="badges"><div><svg><use href="#i-leak"/></svg>LEAK PROOF</div><div><svg><use href="#i-recycle"/></svg>RECYCLABLE</div><div><svg><use href="#i-bpa"/></svg>BPA FREE</div><div><svg><use href="#i-micro"/></svg>MICROWAVE SAFE</div></div></div>
    </article>
  </div>
</section>

<!-- Custom printing & news spread -->
<section class="spread spread--extras">
  <div class="page">
    <div class="band band--left">Custom Printing</div>
    <svg class="collage" viewBox="0 0 356.5 359" role="img" aria-label="Collage of custom printed kraft boxes, cups and cutlery">
      <defs><linearGradient id="kraft" x1="1" y1="0" x2="0" y2="1"><stop offset="0" stop-color="#e8c79a"/><stop offset=".6" stop-color="#c99a63"/><stop offset="1" stop-color="#a97a48"/></linearGradient></defs>
      <polygon points="344,79 80,345 344,345" fill="url(#kraft)"/>
    </svg>
    <div class="pitch">
      <span class="kicker">Ready to take your brand to the next level?</span>
      <p>Our custom printing services for disposable food boxes are here to make your packaging pop!</p>
      <p>Why choose us?</p>
      <p><strong>Vibrant Colors:</strong>Stand out with eye-catching designs that grab attention.</p>
      <p><strong>High-Quality Printing:</strong><span style="display:block;width:205px">Get crisp, clear images that showcase your brand beautifully.</span></p>
      <p><strong>Branding and Logos:</strong><span style="display:block;width:165px">Make your mark with custom logos and branding that customers won't forget.</span></p>
      <p class="narrow">From food trucks to catering businesses, our custom printed food boxes are a game-changer! Let your packaging do the talking and leave a lasting impression on your customers.</p>
      <p class="narrow" style="width:90px"><strong>Get in touch today and let's elevate your brand!</strong></p>
    </div>
  </div>

  <div class="page">
    <div class="band band--right">News</div>
    <article class="news-col" style="left:9px">
      <h3>Headline</h3>
      <p>Lorem ipsum dolor sit amet, consectetur adipiscing elit, sed do eiusmod tempor incididunt ut labore et dolore magna aliqua. Ut enim ad minim veniam, quis nostrud exercitation ullamco laboris nisi ut aliquip ex ea commodo consequat. Duis aute irure dolor in</p>
      <div class="wrap"><p style="width:70px">Sed ut perspiciatis unde omnis iste natus error sit voluptatem accusantium doloremque laudantium, totam rem aperiam, eaque ipsa quae ab illo inventore veritatis et quasi architecto beatae vitae dicta sunt explicabo. Nemo enim ipsam voluptatem quia voluptas sit aspernatur aut odit aut fugit, sed quia consequuntur magni dolores eos qui ratione voluptatem sequi nesciunt. Neque porro quisquam est, qui dolorem ipsum quia dolor sit amet, consectetur, adipisci velit, sed quia non numquam eius modi</p></div>
      <p>Sed ut perspiciatis unde omnis iste natus error sit voluptatem accusantium doloremque laudantium, totam rem aperiam, eaque ipsa quae ab illo inventore veritatis et quasi architecto beatae vitae dicta sunt explicabo. Nemo enim ipsam voluptatem quia voluptas sit aspernatur aut odit aut fugit, sed quia consequuntur magni dolores eos qui ratione voluptatem sequi nesciunt. Neque porro quisquam est, qui dolorem ipsum quia dolor sit amet, consectetur, adipisci velit, sed quia non.</p>
    </article>
    <article class="news-col" style="left:182px">
      <h3>Headline</h3>
      <p>Lorem ipsum dolor sit amet, consectetur adipiscing elit, sed do eiusmod tempor incididunt ut labore et dolore magna aliqua. Ut enim ad minim veniam, quis nostrud exercitation ullamco laboris nisi ut aliquip ex ea commodo consequat. Duis aute irure dolor in</p>
      <div class="wrap"><p style="width:70px;margin-left:80px">Sed ut perspiciatis unde omnis iste natus error sit voluptatem accusantium doloremque laudantium, totam rem aperiam, eaque ipsa quae ab illo inventore veritatis et quasi architecto beatae vitae dicta sunt explicabo. Nemo enim ipsam voluptatem quia voluptas sit aspernatur aut odit aut fugit, sed quia consequuntur magni dolores eos qui ratione voluptatem sequi nesciunt. Neque porro quisquam est, qui dolorem ipsum quia dolor sit amet, consectetur, adipisci velit, sed quia non numquam eius modi</p></div>
      <p>Sed ut perspiciatis unde omnis iste natus error sit voluptatem accusantium doloremque laudantium, totam rem aperiam, eaque ipsa quae ab illo inventore veritatis et quasi architecto beatae vitae dicta sunt explicabo. Nemo enim ipsam voluptatem quia voluptas sit aspernatur aut odit aut fugit, sed quia consequuntur magni dolores eos qui ratione voluptatem sequi nesciunt. Neque porro quisquam est, qui dolorem ipsum quia dolor sit amet, consectetur, adipisci velit, sed quia non.</p>
    </article>
    <div class="news-photo" role="img" aria-label="Stacked black takeout containers with clear lids and a noodle meal"></div>
  </div>
</section>
</body>
</html>
```